Webdesign für Holding-Firma
Zielgruppe
Die velunto Holding ist eine Holding-Firma mit drei Tochtergesellschaften: velunto trusted advisors, velutno Real estate und Velunto GmbH. Wir haben Beteiligungen in IT-Unternehmen, Real Estate sowie kleine und mittlere Startups.
Aufgabenstellung
Das Design sollte nicht zu bunt sein und eher schlicht und futuristisch gestaltet sein. Gerne können die Farben aus den verschiedenen Logos verarbeitet werden.

```html
<!DOCTYPE html>
<html lang="de">
<head>
<meta charset="utf-8">
<title>Velunto Group</title>
<link href="https://fonts.googleapis.com/css2?family=Josefin+Sans:wght@300;400;600;700&display=swap" rel="stylesheet">
<style>
:root{
  --ink:#2d3238;
  --dark:#2d3238;
  --light:#f3f3f3;
  --white:#ffffff;
  --field:#f3f3f3;
  --muted:#8a8d91;
  --holding:#e9552b;
  --advisors:#f2b500;
  --estate:#7cc241;
}
*{margin:0;padding:0;box-sizing:border-box}
html,body{width:909px;height:1200px;overflow:hidden}
body{position:relative;background:var(--white);font-family:"Josefin Sans",sans-serif;color:var(--ink)}
.abs{position:absolute}
.hero-visual{left:0;top:0;width:909px;height:480px;background:linear-gradient(180deg,#ededed 0%,#d9dde2 45%,#9aa6b3 75%,#b8c0c8 100%)}
.brand{left:103px;top:32px;font-size:16px;font-weight:600;letter-spacing:1.5px;display:flex;align-items:center;gap:6px}
.brand-mark{width:14px;height:14px;border:2px solid var(--ink);border-radius:50%}
.lang{left:755px;top:35px;font-size:9px;letter-spacing:.5px}
.menu{left:797px;top:37px;width:8px}
.menu span{display:block;height:1px;background:var(--ink);margin-bottom:2px}
.hero-kicker{left:129px;top:160px;font-size:9px;letter-spacing:.6px}
.hero-title{left:129px;top:172px;font-size:18.5px;font-weight:600;letter-spacing:1.6px}
.hero-sub{left:129px;top:205px;font-size:8.6px;line-height:11px;letter-spacing:.5px}
.scroll{left:127px;top:400px}
.group{left:0;top:435px;width:909px;height:380px;background:var(--light);border-radius:54px 54px 0 0}
.group-title{left:104px;top:510px;border-left:1.5px solid var(--ink);padding-left:8px;height:38px;font-size:18px;font-weight:600;letter-spacing:1.5px;line-height:19px}
.card-img{width:149px;height:80px;border-radius:6px}
.card-box{width:161px;height:108px;background:var(--white);border-radius:6px}
.card-logo{width:149px;display:flex;align-items:center;justify-content:center;gap:6px;font-size:11px;font-weight:700;letter-spacing:.5px}
.card-logo i{display:block;width:10px;height:10px}
.btn{background:var(--dark);color:var(--white);border-radius:14px;font-size:7.2px;font-weight:700;letter-spacing:1px;display:flex;align-items:center;gap:10px}
.card-btn{width:113px;height:25px;padding-left:10px}
.contact{left:0;top:761px;width:909px;height:440px;background:var(--white);border-radius:54px 54px 0 0}
.field{background:var(--field);border-radius:4px;font-size:8.4px;letter-spacing:.6px;color:var(--muted);padding:10px 9px}
.send{left:120px;top:994px;width:511px;height:25px;justify-content:center}
.kontakt-title{left:656px;top:836px;border-left:1.5px solid var(--ink);padding-left:7px;font-size:17px;font-weight:600;letter-spacing:1.2px;line-height:17px}
.kontakt-info{left:664px;top:876px;font-size:8.6px;line-height:11px;letter-spacing:.5px}
.kontakt-info b{font-weight:700}
.kontakt-info .row{display:flex;align-items:center;gap:6px;height:15.7px}
.kontakt-info .gap{height:14px}
.link{border-bottom:.6px solid var(--ink)}
.footer{left:0;top:1094px;width:909px;height:106px;background:var(--dark);border-radius:54px 54px 0 0;color:var(--white)}
.footer-rule{left:119px;top:35px;width:702px;height:1px;background:#6d7278}
.copyright{left:122px;top:47px;font-size:7.8px;font-weight:300}
.legal{left:708px;top:47px;font-size:7.8px;font-weight:300;display:flex;gap:8px;align-items:center}
.legal i{display:block;width:8px;height:8px;border:.8px solid var(--white);border-radius:50%}
</style>
</head>
<body>
<header>
  <div class="abs hero-visual" role="img" aria-label="Foto: Geschäftsmann im Anzug auf einem Balkon mit Blick auf eine Hochhaus-Skyline"></div>
  <div class="abs brand"><span class="brand-mark"></span>Velunto</div>
  <div class="abs lang">DE | EN</div>
  <div class="abs menu"><span></span><span></span><span></span></div>
  <p class="abs hero-kicker">Velunto group</p>
  <h1 class="abs hero-title">ENTERPRISE CLOUD BUSINESS</h1>
  <p class="abs hero-sub">Seed und Early-Stage Investments in B2B-StartUps mit best-in-class<br>Cloud-Technologien / real estate investments / familiy office advisory</p>
  <svg class="abs scroll" width="16" height="22" viewBox="0 0 16 22" fill="none" stroke="#2d3238" stroke-width=".8"><line x1="8" y1="0" x2="8" y2="14"/><circle cx="8" cy="15" r="6"/><path d="M5.5 15 8 17.5 10.5 15"/></svg>
</header>

<section class="abs group">
</section>
<h2 class="abs group-title">VELUNTO<br>group</h2>

<div class="abs card-box" style="left:259px;top:566px"></div>
<div class="abs card-img" style="left:259px;top:510px;background:linear-gradient(180deg,#dfe3e6,#6f757b)" role="img" aria-label="Foto: Team am Konferenztisch in einem Glasbüro"></div>
<div class="abs card-logo" style="left:259px;top:618px"><i style="background:var(--holding)"></i>velunto Holding</div>
<div class="abs btn card-btn" style="left:259px;top:662px">MEHR ERFAHREN <span>⟶</span></div>

<div class="abs card-box" style="left:451px;top:566px"></div>
<div class="abs card-img" style="left:451px;top:510px;background:linear-gradient(160deg,#c99a5f,#2e3a55 60%,#d8d8d8)" role="img" aria-label="Foto: Berater besprechen Unterlagen am Tisch"></div>
<div class="abs card-logo" style="left:451px;top:618px"><i style="background:var(--advisors)"></i>velunto trusted advisors</div>
<div class="abs btn card-btn" style="left:451px;top:662px">MEHR ERFAHREN <span>⟶</span></div>

<div class="abs card-box" style="left:643px;top:566px"></div>
<div class="abs card-img" style="left:643px;top:510px;background:linear-gradient(160deg,#a9c4d2,#dfe9ee 55%,#b9bcc0)" role="img" aria-label="Foto: Hausmodell auf einem Tisch mit Vertragsunterlagen"></div>
<div class="abs card-logo" style="left:643px;top:618px"><i style="background:var(--estate)"></i>velutno Real estate</div>
<div class="abs btn card-btn" style="left:643px;top:662px">MEHR ERFAHREN <span>⟶</span></div>

<section class="abs contact"></section>
<div class="abs field" style="left:120px;top:837px;width:249px;height:29px">Name</div>
<div class="abs field" style="left:382px;top:837px;width:249px;height:29px">E-Mail</div>
<div class="abs field" style="left:120px;top:878px;width:511px;height:103px">Mitteilung</div>
<div class="abs btn send">ABSENDEN <span>⟶</span></div>

<h2 class="abs kontakt-title">Kontakt</h2>
<address class="abs kontakt-info" style="font-style:normal">
  <b>Velunto Holding GmbH</b><br>Lindenweg 12<br>77600 Talheim
  <div class="gap"></div>
  <div class="row"><svg width="12" height="9" viewBox="0 0 12 9" fill="none" stroke="#2d3238" stroke-width=".7"><rect x=".5" y=".5" width="11" height="8"/><path d="M.5 .5 6 5l5.5-4.5"/></svg>kontakt@velunto.de</div>
  <div class="row"><svg width="12" height="11" viewBox="0 0 12 11" fill="none" stroke="#2d3238" stroke-width=".7"><path d="M2 1 4 3 3 4.5c1 1.8 2 2.8 3.5 3.5L8 7l2 2-1.5 1.5C4.5 10 1 6 .5 2.5Z"/></svg>+49 (7000) 482 915 60</div>
  <div class="row"><svg width="12" height="12" viewBox="0 0 12 12" fill="none" stroke="#2d3238" stroke-width=".7"><path d="M6 9S2.8 5.8 2.8 3.8a3.2 3.2 0 0 1 6.4 0C9.2 5.8 6 9 6 9Z"/><circle cx="6" cy="3.8" r="1.1"/><path d="M1 11.5 2.5 8h7L11 11.5Z"/></svg><span class="link">Anfahrt &gt;</span></div>
  <div class="gap" style="height:9px"></div>
  <b>Rechtliches</b><br>GF: Jonas Feld und Lena Feld<br>HRB 401122<br>Steuer-Nr.: 12345/67890
</address>

<footer class="abs footer">
  <div class="abs footer-rule"></div>
  <p class="abs copyright">© Copyright © 2020 Velunto Holding GmbH. Alle Rechte vorbehalten.</p>
  <nav class="abs legal"><span>Impressum</span><span>Datenschutz</span><i></i><i></i></nav>
</footer>
</body>
</html>
```